Ridgeline Outfitters Business Cards

Recently had a logo done with Artfolio and now looking for a business card to go along with it.

Target Market(s)

Ridgeline Outfitters is a weapons dealer. My market will be primarily men, hunting, shooting type.

Industry/Entity Type

Business

Contact Information for Business Card

I selected double sided, but this is not required, single or double is going to be fine. I picture the logo on one side, or perhaps just the circle which contains "RO" with the remaining info on the other side.

Font styles to use
Sans Serif

Requirements
Must have
• My name: Milo Brandt
• Title: Owner
• tel: 612-555-0187
• web: www.ridgelineoutfittersmn.example
Nice to have
• I like the concept of a black business card. I would like to keep the colors monotone, black, grey, white or red. Red is acceptable because it is in the logo. I have also seen cards that are matte black with shiny black as well, perhaps for the logo (or circle RO) part of the logo.
• I will upload a couple of the logos for use, and also an example I just found of the black on black. and some others that have a nice contrast.
Should not have
• lots of colors are not wanted.

```html
<!DOCTYPE html>
<html lang="en">
<head>
<meta charset="utf-8">
<title>Ridgeline Outfitters Business Cards</title>
<link href="https://fonts.googleapis.com/css2?family=Montserrat:wght@400;600&display=swap" rel="stylesheet">
<style>
  :root {
    --backdrop: #e9e6e1;
    --card-black: #232323;
    --brand-red: #d9222a;
    --text-grey: #8a8a8a;
    --ring-grey: #9a9a9a;
  }
  html, body {
    margin: 0;
    width: 1200px;
    height: 801px;
    overflow: hidden;
    background: var(--backdrop);
    font-family: "Montserrat", sans-serif;
  }
  .sheet {
    position: relative;
    width: 1200px;
    height: 801px;
  }
  .card {
    position: absolute;
    left: 340px;
    width: 520px;
    height: 297px;
    background: var(--card-black);
    border-radius: 3px;
    box-shadow: 0 10px 24px rgba(0,0,0,0.25);
  }
  .card--front { top: 72px; }
  .card--back { top: 432px; }

  .brand {
    position: absolute;
    display: flex;
    align-items: center;
  }
  .brand__mark {
    border-radius: 50%;
    border: 3px solid var(--ring-grey);
    box-sizing: border-box;
  }
  .brand__name {
    color: var(--brand-red);
    font-weight: 600;
    text-transform: uppercase;
    letter-spacing: 0.06em;
  }
  .card--front .brand {
    left: 60px;
    top: 112px;
    gap: 22px;
  }
  .card--front .brand__mark { width: 72px; height: 72px; }
  .card--front .brand__name { font-size: 26px; }

  .card--back .brand {
    left: 26px;
    top: 66px;
    gap: 12px;
  }
  .card--back .brand__mark { width: 40px; height: 40px; border-width: 2px; }
  .card--back .brand__name { font-size: 13px; }

  .contact {
    position: absolute;
    left: 262px;
    top: 132px;
    color: var(--text-grey);
  }
  .contact__name {
    margin: 0;
    font-size: 22px;
    font-weight: 400;
    letter-spacing: 0.02em;
  }
  .contact__title {
    margin: 0 0 16px;
    color: var(--brand-red);
    font-size: 12px;
  }
  .contact__list {
    list-style: none;
    margin: 0;
    padding: 0;
    font-size: 12.5px;
  }
  .contact__item {
    display: flex;
    align-items: center;
    gap: 10px;
    margin-bottom: 9px;
  }
  .contact__icon {
    width: 12px;
    height: 12px;
    fill: var(--brand-red);
    flex: none;
  }
</style>
</head>
<body>
<main class="sheet">
  <section class="card card--front" aria-label="Card front">
    <div class="brand">
      <span class="brand__mark" aria-hidden="true"></span>
      <span class="brand__name">Ridgeline Outfitters</span>
    </div>
  </section>

  <section class="card card--back" aria-label="Card back">
    <div class="brand">
      <span class="brand__mark" aria-hidden="true"></span>
      <span class="brand__name">Ridgeline Outfitters</span>
    </div>
    <div class="contact">
      <h1 class="contact__name">Milo Brandt</h1>
      <p class="contact__title">Owner</p>
      <ul class="contact__list">
        <li class="contact__item">
          <svg class="contact__icon" viewBox="0 0 12 12" aria-hidden="true"><path d="M1 3.5C1 2 2.5 1.5 6 1.5S11 2 11 3.5V5H8.5V4H3.5V5H1Z"/><rect x="2.5" y="6" width="7" height="5" rx="1"/></svg>
          <span>612-555-0187</span>
        </li>
        <li class="contact__item">
          <svg class="contact__icon" viewBox="0 0 12 12" aria-hidden="true"><path d="M0.5 2.5H11.5V9.5H0.5Z M1.5 3.3L6 6.6L10.5 3.3" stroke="#232323" stroke-width="0.9"/></svg>
          <span>yourname@example.com</span>
        </li>
        <li class="contact__item">
          <svg class="contact__icon" viewBox="0 0 12 12" aria-hidden="true"><circle cx="6" cy="6" r="5.3" fill="none" stroke="#d9222a" stroke-width="1.2"/><ellipse cx="6" cy="6" rx="2.2" ry="5.3" fill="none" stroke="#d9222a" stroke-width="1"/><path d="M0.7 6H11.3" stroke="#d9222a" stroke-width="1"/></svg>
          <span>www.ridgelineoutfittersmn.example</span>
        </li>
      </ul>
    </div>
  </section>
</main>
</body>
</html>
```